PowerPoint design MedoraVix

We need a PowerPoint set-up based upon our existing logo (see joint file)
Our company is operating in the health care and life science sector. We are mainly focussing on international business

Target Market(s)

International

Industry/Entity Type

health care and life sciences

Requirements
Must have
• Logos as added

```html
<!DOCTYPE html>
<html lang="en">
<head>
<meta charset="utf-8">
<title>MedoraVix – Presentation Template</title>
<link href="https://fonts.googleapis.com/css2?family=Montserrat:wght@400;500;600;700&display=swap" rel="stylesheet">
<style>
  :root{
    --navy:#0d4a86;
    --navy-deep:#0a3e72;
    --green:#5cbc22;
    --ink:#3f3f46;
    --grey:#7a7a80;
    --charcoal:#4a4a4e;
    --paper:#ffffff;
    --stage:#e6e9ee;
    --board:#d9d9dd;
    --strip:#f1f1f2;
  }
  *{box-sizing:border-box;margin:0;padding:0}
  html,body{width:682px;height:1200px;overflow:hidden}
  body{position:relative;background:var(--board);font-family:"Montserrat",Arial,sans-serif;color:var(--ink)}

  .hero{position:absolute;left:0;top:0;width:682px;height:407px;background:linear-gradient(180deg,#dfe3e9 0%,#eef0f3 100%)}
  .hero-brand{position:absolute;left:500px;top:48px;display:flex;align-items:center;gap:10px}
  .hero-brand .dot{width:32px;height:32px;border-radius:50%;background:var(--navy)}
  .hero-brand .name{font-size:22px;font-weight:600;color:var(--navy)}

  .frame{position:absolute;overflow:hidden;box-shadow:0 2px 6px rgba(0,0,0,.12)}
  .slide{position:absolute;left:0;top:0;width:683px;height:383px;background:var(--paper);overflow:hidden;transform-origin:0 0}
  .s-sm{transform:scale(.4685)}
  .s-hero{transform:scale(.5564)}
  .abs{position:absolute}

  /* brand lockup */
  .brand{position:absolute;display:flex;align-items:center;gap:10px}
  .brand .dot{width:50px;height:50px;border-radius:50%;background:var(--navy)}
  .brand .name{font-size:29px;font-weight:600;color:var(--navy)}

  /* title slide */
  .t-title{left:53px;top:148px;font-size:35px;line-height:36px;font-weight:600;color:var(--navy)}
  .t-sub{left:53px;top:226px;font-size:15px;color:var(--green)}
  .t-date{left:53px;top:277px;width:153px;height:22px;background:var(--navy);border-radius:2px;color:#fff;font-size:8.5px;display:flex;align-items:center;justify-content:center}
  .strip{left:0;bottom:0;width:683px;height:20px;background:var(--strip);font-size:8px;color:var(--grey);display:flex;align-items:center;justify-content:center}
  .art{position:absolute;left:0;top:0}

  /* footer */
  .foot .dot{position:absolute;left:16px;top:344px;width:22px;height:22px;border-radius:50%;background:var(--navy)}
  .foot .name{position:absolute;left:44px;top:343px;font-size:14px;font-weight:600;color:var(--navy)}
  .foot .bar{position:absolute;left:122px;top:351px;width:561px;height:10px;border-radius:5px 0 0 5px;background:linear-gradient(90deg,var(--navy),var(--green))}
  .foot .page{position:absolute;left:642px;top:345px;width:22px;height:22px}
  .foot .page::before{content:"";position:absolute;inset:1px;background:var(--navy);border:2px solid #fff;transform:rotate(45deg)}
  .foot .page span{position:relative;display:block;text-align:center;line-height:22px;font-size:8px;font-weight:600;color:#fff}

  /* content slides */
  .h-slide{font-size:28px;font-weight:500;color:var(--ink);line-height:32px}
  .lead{font-size:10px;line-height:11px;font-weight:600;color:var(--navy)}
  .body{font-size:8px;line-height:9px;color:var(--grey)}
  .body p{margin-bottom:8px}
  .bullets{list-style:none}
  .bullets li{position:relative;padding-left:16px;margin-bottom:8px}
  .bullets li::before{content:"";position:absolute;left:0;top:3px;width:4px;height:4px;border-radius:50%;background:var(--green)}

  .photo{position:absolute}
  .band-blue{left:477px;top:0;width:206px;height:383px;background:linear-gradient(180deg,#1a5d9b,var(--navy-deep))}

  /* team */
  .team-band{left:0;top:0;width:683px;height:143px;background:linear-gradient(100deg,var(--navy) 0%,#1f6a7d 45%,#3a8c4a 75%,#69b24a 100%)}
  .team-head{left:0;top:22px;width:683px;text-align:center;font-size:26px;font-weight:500;color:#fff}
  .member{position:absolute;top:81px;width:180px;text-align:center}
  .member .portrait{width:96px;height:124px;margin:0 auto;background:linear-gradient(180deg,#f4f4f4,#dcdcdc)}
  .member .who{margin-top:8px;font-size:15px;font-weight:500}
  .member .role{font-size:9px;color:var(--grey);margin-top:3px}
  .member .body{margin-top:10px;text-align:center}

  /* features */
  .center-title{left:0;top:22px;width:683px;text-align:center;font-size:26px;font-weight:500;color:var(--ink)}
  .feat{position:absolute;width:190px}
  .feat h3{font-size:15px;font-weight:500;line-height:18px}
  .feat .body{margin-top:3px}
  .feat.l{left:65px;text-align:right}
  .feat.r{left:428px}
  .icon{position:absolute;width:50px;height:50px;border-radius:50%;display:flex;align-items:center;justify-content:center}

  .navy{color:var(--navy)} .green{color:var(--green)} .dark{color:var(--charcoal)}
  .bg-navy{background:var(--navy)} .bg-green{background:var(--green)} .bg-dark{background:var(--charcoal)}

  /* chart */
  .legend{position:absolute;left:434px;width:200px}
  .legend h3{display:flex;align-items:center;gap:8px;font-size:11px;font-weight:500}
  .legend h3 i{width:15px;height:15px;border-radius:2px;display:inline-block}
  .legend .body{margin:6px 0 0 23px}

  /* contact */
  .contact-title{left:346px;top:162px;font-size:18px;font-weight:500;color:var(--ink)}
  .contact-addr{left:346px;top:189px;font-size:8px;color:var(--ink)}
  .contact-list{left:346px;top:212px;list-style:none;font-size:8px;color:var(--ink)}
  .contact-list li{display:flex;align-items:center;gap:8px;height:19px}
</style>
</head>
<body>

<!-- presentation cover, shown large -->
<section class="hero">
  <div class="hero-brand"><span class="dot"></span><span class="name">MedoraVix</span></div>
  <div class="frame" style="left:80px;top:120px;width:380px;height:213px">
    <div class="slide s-hero">
      <svg class="art" width="683" height="383" viewBox="0 0 683 383" aria-hidden="true">
        <defs>
          <linearGradient id="gDocA" x1="0" y1="0" x2="1" y2="1">
            <stop offset="0" stop-color="#dfe9f0"/><stop offset=".5" stop-color="#c6d6df"/><stop offset="1" stop-color="#c9e2c3"/>
          </linearGradient>
        </defs>
        <circle cx="565" cy="130" r="205" fill="url(#gDocA)" role="img" aria-label="Photo: doctor in a white coat holding a red stethoscope"/>
        <circle cx="565" cy="130" r="210" fill="none" stroke="var(--navy)" stroke-width="8"/>
        <path d="M746.9 235 A210 210 0 0 1 510.6 332.8" fill="none" stroke="var(--green)" stroke-width="12"/>
        <circle cx="510.6" cy="332.8" r="18" fill="var(--green)"/>
      </svg>
      <div class="brand" style="left:52px;top:65px"><span class="dot"></span><span class="name">MedoraVix</span></div>
      <div class="abs t-title">Presentation<br>Title Goes Here!</div>
      <div class="abs t-sub">Subtitle of Presentation Goes Here!</div>
      <div class="abs t-date">Thursday, March 24, 2022</div>
      <div class="abs strip">© 2022 MedoraVix, All Rights Reserved.</div>
    </div>
  </div>
</section>

<!-- 1: cover A -->
<div class="frame" style="left:16px;top:430px;width:320px;height:180px">
  <div class="slide s-sm">
    <svg class="art" width="683" height="383" viewBox="0 0 683 383" aria-hidden="true">
      <defs>
        <linearGradient id="gDocB" x1="0" y1="0" x2="1" y2="1">
          <stop offset="0" stop-color="#dfe9f0"/><stop offset=".5" stop-color="#c6d6df"/><stop offset="1" stop-color="#c9e2c3"/>
        </linearGradient>
      </defs>
      <circle cx="565" cy="130" r="205" fill="url(#gDocB)" role="img" aria-label="Photo: doctor in a white coat holding a red stethoscope"/>
      <circle cx="565" cy="130" r="210" fill="none" stroke="var(--navy)" stroke-width="8"/>
      <path d="M746.9 235 A210 210 0 0 1 510.6 332.8" fill="none" stroke="var(--green)" stroke-width="12"/>
      <circle cx="510.6" cy="332.8" r="18" fill="var(--green)"/>
    </svg>
    <div class="brand" style="left:52px;top:65px"><span class="dot"></span><span class="name">MedoraVix</span></div>
    <div class="abs t-title">Presentation<br>Title Goes Here!</div>
    <div class="abs t-sub">Subtitle of Presentation Goes Here!</div>
    <div class="abs t-date">Thursday, March 24, 2022</div>
    <div class="abs strip">© 2022 MedoraVix, All Rights Reserved.</div>
  </div>
</div>

<!-- 2: cover B -->
<div class="frame" style="left:346px;top:430px;width:320px;height:180px">
  <div class="slide s-sm">
    <svg class="art" width="683" height="383" viewBox="0 0 683 383" aria-hidden="true">
      <defs>
        <linearGradient id="gLab" x1="0" y1="0" x2="1" y2="1">
          <stop offset="0" stop-color="#e8ecee"/><stop offset=".5" stop-color="#d6dde3"/><stop offset="1" stop-color="#cfe0cc"/>
        </linearGradient>
      </defs>
      <circle cx="565" cy="130" r="205" fill="url(#gLab)" role="img" aria-label="Photo: pharmacist in a face mask and lab coat"/>
      <circle cx="565" cy="130" r="210" fill="none" stroke="var(--navy)" stroke-width="8"/>
      <path d="M746.9 235 A210 210 0 0 1 510.6 332.8" fill="none" stroke="var(--green)" stroke-width="12"/>
      <circle cx="510.6" cy="332.8" r="18" fill="var(--green)"/>
    </svg>
    <div class="brand" style="left:52px;top:65px"><span class="dot"></span><span class="name">MedoraVix</span></div>
    <div class="abs t-title">Presentation<br>Title Goes Here!</div>
    <div class="abs t-sub">Subtitle of Presentation Goes Here!</div>
    <div class="abs t-date">Thursday, March 24, 2022</div>
    <div class="abs strip">© 2022 MedoraVix, All Rights Reserved.</div>
  </div>
</div>

<!-- 3: text with image -->
<div class="frame" style="left:16px;top:620px;width:320px;height:180px">
  <div class="slide s-sm">
    <div class="photo" style="left:28px;top:0;width:252px;height:318px;background:linear-gradient(160deg,#cfe3e6,#a9c9cf 55%,#e4eef0)" role="img" aria-label="Photo: doctor with arms crossed holding a stethoscope"></div>
    <div class="abs h-slide" style="left:313px;top:38px">Slide Title Goes Here</div>
    <div class="abs lead" style="left:313px;top:92px;width:340px">Lorem ipsum dolor sit amet, consectetur adipiscing elit. Vivamus eu dui ex. Curabitur dapibus dignissim dui, in molestie metus feugiat sed. Praesent aliquet lorem ex.</div>
    <div class="abs body" style="left:313px;top:141px;width:340px">
      <p>Lorem ipsum dolor sit amet, consectetur adipiscing elit. Vivamus eu dui ex. Curabitur dapibus dignissim dui, in molestie metus feugiat sed. Praesent aliquet lorem ex, eu dapibus odio varius at. Duis eget tellus porta, consequat lacus vitae, venenatis dolor.</p>
      <p>Praesent aliquet lorem ex, eu dapibus odio varius at. Duis eget tellus porta, consequat lacus vitae, venenatis dolor. Nulla facilisi. In et sollicitudin lacus. Donec risus orci, gravida sit amet risus vehicula, aliquet pretium sapien.</p>
      <p>Vivamus eu dui ex. Curabitur dapibus dignissim dui, in molestie metus feugiat sed. Praesent aliquet lorem ex, eu dapibus odio varius at. Duis eget tellus porta, consequat lacus vitae, venenatis dolor.</p>
      <p>Nulla facilisi. In et sollicitudin lacus. Donec risus orci, gravida sit amet risus vehicula, aliquet pretium sapien.</p>
    </div>
    <div class="foot"><span class="dot"></span><span class="name">MedoraVix</span><span class="bar"></span><span class="page"><span>3</span></span></div>
  </div>
</div>

<!-- 4: bullets with framed image -->
<div class="frame" style="left:346px;top:620px;width:320px;height:180px">
  <div class="slide s-sm">
    <div class="abs band-blue"></div>
    <div class="photo" style="left:310px;top:38px;width:336px;height:272px;border:2px solid #fff;background:linear-gradient(135deg,#b7c6d2,#7d93a6 50%,#d8dde2)" role="img" aria-label="Photo: hands using a tablet in a clinic"></div>
    <div class="abs h-slide" style="left:40px;top:36px">Slide Title<br>Goes Here</div>
    <div class="abs lead" style="left:40px;top:118px;width:245px">Lorem ipsum dolor sit amet, consectetur adipiscing elit. Vivamus eu dui ex. Curabitur dapibus dignissim dui, in molestie metus feugiat sed. Praesent aliquet lorem ex.</div>
    <ul class="abs body bullets" style="left:40px;top:178px;width:245px">
      <li>Lorem ipsum dolor sit amet, consectetur adipiscing elit. Vivamus eu dui ex. Curabitur dapibus dignissim dui, in molestie metus feugiat sed.</li>
      <li>Praesent aliquet lorem ex, eu dapibus odio varius at. Duis eget tellus porta, consequat lacus vitae, venenatis dolor.</li>
      <li>Nulla facilisi. In et sollicitudin lacus. Donec risus orci, gravida sit amet risus vehicula, aliquet pretium sapien. Lorem ipsum dolor sit amet, consectetur adipiscing elit. Vivamus eu dui ex. Curabitur dapibus dignissim dui, in molestie metus feugiat sed. Curabitur dapibus dignissim dui, in molestie.</li>
    </ul>
    <div class="foot"><span class="dot"></span><span class="name">MedoraVix</span><span class="bar"></span><span class="page"><span>4</span></span></div>
  </div>
</div>

<!-- 5: team -->
<div class="frame" style="left:16px;top:811px;width:320px;height:180px">
  <div class="slide s-sm">
    <div class="abs team-band" role="img" aria-label="Blurred photo of a medical team in blue and green tones"></div>
    <div class="abs team-head">Meet our Team</div>
    <div class="member" style="left:40px">
      <div class="portrait" role="img" aria-label="Portrait photo of team member"></div>
      <div class="who navy">Name Goes Here</div>
      <div class="role">Job Title Goes Here</div>
      <div class="body">Lorem ipsum dolor sit amet, consectetur adipiscing elit. Vivamus eu dui ex. Curabitur dapibus dignissim dui, in molestie metus feugiat sed. Praesent aliquet lorem ex, eu dapibus odio varius at.</div>
    </div>
    <div class="member" style="left:251px">
      <div class="portrait" role="img" aria-label="Portrait photo of team member"></div>
      <div class="who green">Name Goes Here</div>
      <div class="role">Job Title Goes Here</div>
      <div class="body">Lorem ipsum dolor sit amet, consectetur adipiscing elit. Vivamus eu dui ex. Curabitur dapibus dignissim dui, in molestie metus feugiat sed. Praesent aliquet lorem ex, eu dapibus odio varius at.</div>
    </div>
    <div class="member" style="left:462px">
      <div class="portrait" role="img" aria-label="Portrait photo of team member"></div>
      <div class="who dark">Name Goes Here</div>
      <div class="role">Job Title Goes Here</div>
      <div class="body">Lorem ipsum dolor sit amet, consectetur adipiscing elit. Vivamus eu dui ex. Curabitur dapibus dignissim dui, in molestie metus feugiat sed. Praesent aliquet lorem ex, eu dapibus odio varius at.</div>
    </div>
    <div class="foot"><span class="dot"></span><span class="name">MedoraVix</span><span class="bar"></span><span class="page"><span>5</span></span></div>
  </div>
</div>

<!-- 6: features with icons -->
<div class="frame" style="left:346px;top:811px;width:320px;height:180px">
  <div class="slide s-sm">
    <div class="abs center-title">Slide Title Goes Here</div>

    <div class="feat l" style="top:97px"><h3 class="navy">Heading Goes Here</h3><div class="body">Lorem ipsum dolor sit amet, consectetur adipiscing elit. Vivamus eu dui ex. Curabitur dapibus dignissim dui.</div></div>
    <div class="feat l" style="top:175px"><h3 class="dark">Heading Goes Here</h3><div class="body">Lorem ipsum dolor sit amet, consectetur adipiscing elit. Vivamus eu dui ex. Curabitur dapibus dignissim dui.</div></div>
    <div class="feat l" style="top:253px"><h3 class="green">Heading Goes Here</h3><div class="body">Lorem ipsum dolor sit amet, consectetur adipiscing elit. Vivamus eu dui ex. Curabitur dapibus dignissim dui.</div></div>
    <div class="feat r" style="top:97px"><h3 class="green">Heading Goes Here</h3><div class="body">Lorem ipsum dolor sit amet, consectetur adipiscing elit. Vivamus eu dui ex. Curabitur dapibus dignissim dui.</div></div>
    <div class="feat r" style="top:175px"><h3 class="navy">Heading Goes Here</h3><div class="body">Lorem ipsum dolor sit amet, consectetur adipiscing elit. Vivamus eu dui ex. Curabitur dapibus dignissim dui.</div></div>
    <div class="feat r" style="top:253px"><h3 class="dark">Heading Goes Here</h3><div class="body">Lorem ipsum dolor sit amet, consectetur adipiscing elit. Vivamus eu dui ex. Curabitur dapibus dignissim dui.</div></div>

    <span class="icon bg-navy" style="left:273px;top:97px"><svg width="26" height="16" viewBox="0 0 26 16" aria-hidden="true"><path d="M1 2 C8 14 18 14 25 2 M1 14 C8 2 18 2 25 14" fill="none" stroke="#fff" stroke-width="2"/></svg></span>
    <span class="icon bg-dark" style="left:273px;top:175px"><svg width="24" height="20" viewBox="0 0 24 20" aria-hidden="true"><path d="M2 8 H22 A10 10 0 0 1 2 8 Z" fill="#fff"/><path d="M14 8 L20 1" stroke="#fff" stroke-width="2.5"/></svg></span>
    <span class="icon bg-green" style="left:273px;top:253px"><svg width="24" height="20" viewBox="0 0 24 20" aria-hidden="true"><rect x="1" y="5" width="22" height="14" rx="2" fill="#fff"/><rect x="8" y="1" width="8" height="5" rx="1" fill="none" stroke="#fff" stroke-width="2"/><path d="M12 8 V16 M8 12 H16" stroke="var(--green)" stroke-width="2.5"/></svg></span>
    <span class="icon bg-green" style="left:360px;top:97px"><svg width="20" height="24" viewBox="0 0 20 24" aria-hidden="true"><circle cx="10" cy="14" r="5" fill="none" stroke="#fff" stroke-width="2.5"/><path d="M10 2 V10 M3 22 H17" stroke="#fff" stroke-width="2.5"/></svg></span>
    <span class="icon bg-navy" style="left:360px;top:175px"><svg width="20" height="24" viewBox="0 0 20 24" aria-hidden="true"><path d="M7 2 H13 M8 2 V9 L2 21 H18 L12 9 V2" fill="#fff" stroke="#fff" stroke-width="1.5" stroke-linejoin="round"/></svg></span>
    <span class="icon bg-dark" style="left:360px;top:253px"><svg width="22" height="22" viewBox="0 0 22 22" aria-hidden="true"><rect x="2" y="13" width="4" height="7" fill="#fff"/><rect x="9" y="9" width="4" height="11" fill="#fff"/><rect x="16" y="5" width="4" height="15" fill="#fff"/><path d="M2 10 L10 4 L16 2" fill="none" stroke="#fff" stroke-width="1.5"/></svg></span>

    <div class="foot"><span class="dot"></span><span class="name">MedoraVix</span><span class="bar"></span><span class="page"><span>6</span></span></div>
  </div>
</div>

<!-- 7: chart -->
<div class="frame" style="left:16px;top:1001px;width:320px;height:180px">
  <div class="slide s-sm">
    <div class="abs center-title">Slide Title Goes Here</div>
    <svg class="art" width="683" height="383" viewBox="0 0 683 383" aria-label="Bar chart of four categories" role="img">
      <g font-family="Montserrat, Arial, sans-serif" font-size="6" fill="#444" text-anchor="end">
        <text x="62" y="227">0</text><text x="62" y="207">1</text><text x="62" y="187">2</text><text x="62" y="167">3</text><text x="62" y="147">4</text><text x="62" y="127">5</text><text x="62" y="107">6</text>
      </g>
      <g>
        <rect x="82" y="139" width="14" height="86" fill="var(--navy)"/><rect x="100" y="177" width="14" height="48" fill="var(--green)"/><rect x="118" y="185" width="14" height="40" fill="var(--charcoal)"/>
        <rect x="162" y="175" width="14" height="50" fill="var(--navy)"/><rect x="180" y="137" width="14" height="88" fill="var(--green)"/><rect x="198" y="185" width="14" height="40" fill="var(--charcoal)"/>
        <rect x="242" y="155" width="14" height="70" fill="var(--navy)"/><rect x="260" y="189" width="14" height="36" fill="var(--green)"/><rect x="278" y="165" width="14" height="60" fill="var(--charcoal)"/>
        <rect x="322" y="135" width="14" height="90" fill="var(--navy)"/><rect x="340" y="169" width="14" height="56" fill="var(--green)"/><rect x="358" y="125" width="14" height="100" fill="var(--charcoal)"/>
      </g>
      <line x1="68" y1="225" x2="390" y2="225" stroke="#bbb" stroke-width=".8"/>
      <g font-family="Montserrat, Arial, sans-serif" font-size="6" fill="#444" text-anchor="middle">
        <text x="107" y="234">Category 1</text><text x="187" y="234">Category 2</text><text x="267" y="234">Category 3</text><text x="347" y="234">Category 4</text>
      </g>
    </svg>
    <div class="abs body" style="left:58px;top:262px;width:330px">Lorem ipsum dolor sit amet, consectetur adipiscing elit. Vivamus eu dui ex. Curabitur dapibus dignissim dui, in molestie metus feugiat sed. Praesent aliquet lorem ex, eu dapibus odio varius at. Duis eget tellus porta, consequat lacus vitae, venenatis dolor. Nulla facilisi. In et sollicitudin lacus. Donec risus orci, gravida sit amet risus vehicula, aliquet pretium sapien.</div>
    <div class="legend" style="top:100px"><h3 class="navy"><i class="bg-navy"></i>Heading Goes Here</h3><div class="body">Lorem ipsum dolor sit amet, consectetur adipiscing elit. Vivamus eu dui ex. Curabitur dapibus dignissim dui, in molestie metus feugiat sed.</div></div>
    <div class="legend" style="top:173px"><h3 class="green"><i class="bg-green"></i>Heading Goes Here</h3><div class="body">Lorem ipsum dolor sit amet, consectetur adipiscing elit. Vivamus eu dui ex. Curabitur dapibus dignissim dui, in molestie metus feugiat sed.</div></div>
    <div class="legend" style="top:246px"><h3 class="dark"><i class="bg-dark"></i>Heading Goes Here</h3><div class="body">Lorem ipsum dolor sit amet, consectetur adipiscing elit. Vivamus eu dui ex. Curabitur dapibus dignissim dui, in molestie metus feugiat sed.</div></div>
    <div class="foot"><span class="dot"></span><span class="name">MedoraVix</span><span class="bar"></span><span class="page"><span>7</span></span></div>
  </div>
</div>

<!-- 8: contact -->
<div class="frame" style="left:346px;top:1001px;width:320px;height:180px">
  <div class="slide s-sm">
    <svg class="art" width="683" height="383" viewBox="0 0 683 383" aria-hidden="true">
      <defs>
        <linearGradient id="gTouch" x1="0" y1="0" x2="1" y2="1">
          <stop offset="0" stop-color="#b9cbd6"/><stop offset=".6" stop-color="#dfe8ec"/><stop offset="1" stop-color="#c5dcc2"/>
        </linearGradient>
      </defs>
      <circle cx="70" cy="60" r="144" fill="url(#gTouch)" role="img" aria-label="Photo: hand touching a digital screen"/>
      <circle cx="70" cy="60" r="150" fill="none" stroke="var(--navy)" stroke-width="8"/>
      <path d="M145 -70 A150 150 0 0 1 46.5 208" fill="none" stroke="var(--green)" stroke-width="12"/>
      <circle cx="46.5" cy="206" r="15" fill="var(--green)"/>
    </svg>
    <div class="brand" style="left:346px;top:88px"><span class="dot" style="width:40px;height:40px"></span><span class="name" style="font-size:24px">MedoraVix</span></div>
    <div class="abs contact-title">Contact Us</div>
    <div class="abs contact-addr">Insert Company Address Goes Here!</div>
    <ul class="abs contact-list">
      <li><svg width="10" height="10" viewBox="0 0 10 10" aria-hidden="true"><path d="M2 1 L4 1 L5 3 L4 4 Q5 6 6 6 L7 5 L9 6 L9 8 Q8 9 7 9 Q1 8 1 2 Q1 1 2 1Z" fill="var(--green)"/></svg>Insert Phone Number</li>
      <li><svg width="10" height="10" viewBox="0 0 10 10" aria-hidden="true"><circle cx="5" cy="5" r="4" fill="none" stroke="var(--green)" stroke-width="1.3"/><circle cx="5" cy="5" r="1.6" fill="var(--green)"/></svg>Insert E-Mail Address</li>
      <li><svg width="10" height="10" viewBox="0 0 10 10" aria-hidden="true"><circle cx="5" cy="5" r="4" fill="none" stroke="var(--green)" stroke-width="1"/><ellipse cx="5" cy="5" rx="1.8" ry="4" fill="none" stroke="var(--green)" stroke-width="1"/><path d="M1 5 H9" stroke="var(--green)" stroke-width="1"/></svg>Insert URL Address</li>
    </ul>
    <div class="abs strip">© 2022 MedoraVix, All Rights Reserved.</div>
  </div>
</div>

</body>
</html>
```